Virtual Assistant/Online Marketing Business Card/Stationary

I need a professional but modern business card/stationary for my company in Dallas called Brivolo. Brivolo is a virtual assistant specializing in online marketing. I would like a unique design that stands out and makes my brand clear. Incorporating the logo is a must and have attached it to this brief.

Target Market(s)

small business owners & entrepreneurs, 35-65

Industry/Entity Type

Business

Contact Information for Business Card

Maren Tolk
marentolk@brivolo.biz
(555) 271-9064
brivolo.biz

Font styles to use
Sans Serif

Colors
f04a50
3176b5
9bcb3c

Requirements
Must have
• Colors that match the logo colors. Logo integration

```html
<!DOCTYPE html>
<html lang="en">
<head>
<meta charset="utf-8">
<title>Brivolo Business Card</title>
<link rel="stylesheet" href="https://fonts.googleapis.com/css2?family=PT+Sans:wght@400;700&display=swap">
<style>
  :root {
    --stage: #3a302c;
    --card-dark: #1f1f20;
    --card-green: #72c043;
    --brand-green: #9bcb3c;
    --brand-red: #f04a50;
    --brand-blue: #3176b5;
    --ink-light: #e8e8e8;
    --ink-muted: #d4d4d4;
    --divider: #3a3a3a;
  }
  * { box-sizing: border-box; margin: 0; padding: 0; }
  html, body { width: 1200px; height: 844px; overflow: hidden; }
  body {
    background: var(--stage);
    font-family: "PT Sans", sans-serif;
    display: flex;
    align-items: center;
    justify-content: center;
    gap: 40px;
  }
  .card {
    width: 540px;
    height: 310px;
    border-radius: 4px;
    box-shadow: 0 14px 30px rgba(0,0,0,.45);
    position: relative;
    overflow: hidden;
  }
  .card--front {
    background: var(--card-dark);
    display: flex;
    align-items: center;
  }
  .brand-block {
    width: 260px;
    display: flex;
    align-items: center;
    justify-content: center;
    gap: 12px;
  }
  .brand-mark {
    width: 22px;
    height: 22px;
    border-radius: 50%;
    background: var(--brand-green);
  }
  .brand-name {
    font-weight: 700;
    font-size: 50px;
    color: var(--ink-light);
    letter-spacing: -0.5px;
  }
  .divider {
    width: 1px;
    height: 170px;
    background: var(--divider);
  }
  .contact {
    padding-left: 28px;
  }
  .contact__name {
    font-weight: 700;
    font-size: 21px;
    color: var(--brand-green);
    margin-bottom: 26px;
  }
  .contact__list { list-style: none; }
  .contact__item {
    display: flex;
    align-items: center;
    gap: 12px;
    font-size: 15px;
    color: var(--ink-muted);
    line-height: 24px;
  }
  .contact__icon { width: 13px; height: 13px; fill: var(--brand-green); flex: none; }
  .card--back {
    background: var(--card-green);
    display: flex;
    align-items: center;
    justify-content: center;
    gap: 16px;
  }
  .card--back .brand-mark { width: 30px; height: 30px; background: #ffffff; }
  .card--back .brand-name { color: #ffffff; font-size: 72px; }
</style>
</head>
<body>
  <section class="card card--front" aria-label="Business card front">
    <div class="brand-block">
      <span class="brand-mark"></span>
      <span class="brand-name">Brivolo</span>
    </div>
    <div class="divider"></div>
    <div class="contact">
      <p class="contact__name">Maren Tolk</p>
      <ul class="contact__list">
        <li class="contact__item">
          <svg class="contact__icon" viewBox="0 0 24 24" aria-hidden="true"><path d="M6.6 10.8a15.1 15.1 0 0 0 6.6 6.6l2.2-2.2a1 1 0 0 1 1-.25 11.4 11.4 0 0 0 3.6.57 1 1 0 0 1 1 1V20a1 1 0 0 1-1 1A17 17 0 0 1 3 4a1 1 0 0 1 1-1h3.5a1 1 0 0 1 1 1c0 1.25.2 2.45.57 3.57a1 1 0 0 1-.25 1z"/></svg>
          (555) 271-9064
        </li>
        <li class="contact__item">
          <svg class="contact__icon" viewBox="0 0 24 24" aria-hidden="true"><path d="M2 5h20v14H2z M3.5 6.5 12 13l8.5-6.5" fill="var(--brand-green)"/><path d="M3 6l9 7 9-7" fill="none" stroke="#1f1f20" stroke-width="2"/></svg>
          marentolk@brivolo.biz
        </li>
        <li class="contact__item">
          <svg class="contact__icon" viewBox="0 0 24 24" aria-hidden="true"><circle cx="12" cy="12" r="10"/><path d="M2 12h20M12 2c3 3 3 17 0 20M12 2c-3 3-3 17 0 20" fill="none" stroke="#1f1f20" stroke-width="1.6"/></svg>
          www.brivolo.biz
        </li>
      </ul>
    </div>
  </section>

  <section class="card card--back" aria-label="Business card back">
    <span class="brand-mark"></span>
    <span class="brand-name">Brivolo</span>
  </section>
</body>
</html>
```